Business Card Design

RETAIL HIGH END CONTEMPORARY WOMEN'S CLOTHING STORE
MODERN, SIMPLE, CLEAN, COOL

WE ARE ALL ABOUT NY and CALIF STYLE.... CLASSY but EDGY..
COOLEST DENIM , Trendsetting, NEUTRAL Pallettes,
Collections : Fig and Stone, Dorian Vesk, PMW, K47, QTB
Don't need names of collections on card. thats just good info
for designer of card.

WOULD LIKE THE FONT TO BE INTERESTING, but CLEAN
We are on facebook daily with photos of outfits we put together
which you can look up and friend us.... MolvaHarbor
Also on instagram .
Open to options on color and size, but need cool and fresh.

Contact Information for Business Card

DELLA 5417 Larkmoor Rd. #309 Ember Court Arcade..Va. Beach, Va. 23987
Phone 757.386.5049 Fax 757.386-2613 EMAIL..DELLAMODE@QUILLBOX.COM

```html
<!DOCTYPE html>
<html lang="en">
<head>
<meta charset="utf-8">
<title>DELLA — Business Card</title>
<link href="https://fonts.googleapis.com/css2?family=Jost:wght@300;400&display=swap" rel="stylesheet">
<style>
  :root {
    --backdrop: #2b2b2c;
    --card-base: #141414;
    --card-edge: #0a0a0a;
    --pattern-tone: #262626;
    --ink: #e9e9e9;
    --logo-ink: #ffffff;
    --accent: #8cc63f;
  }
  html, body {
    margin: 0;
    padding: 0;
    width: 1200px;
    height: 800px;
    overflow: hidden;
    background: var(--backdrop);
  }
  .canvas {
    position: relative;
    width: 1200px;
    height: 800px;
    display: flex;
    align-items: center;
    justify-content: center;
  }
  .business-card {
    position: relative;
    width: 840px;
    height: 480px;
    background: var(--card-base);
    overflow: hidden;
    font-family: "Jost", "Futura", sans-serif;
    font-weight: 300;
    color: var(--ink);
  }
  .card-pattern {
    position: absolute;
    inset: 0;
    background:
      radial-gradient(circle at 30% 60%, var(--pattern-tone) 0%, transparent 38%),
      radial-gradient(circle at 75% 35%, var(--pattern-tone) 0%, transparent 32%),
      linear-gradient(160deg, #1b1b1b 0%, var(--card-base) 55%, var(--card-edge) 100%);
  }
  .brand-name {
    position: absolute;
    top: 105px;
    left: 0;
    right: 0;
    margin: 0;
    text-align: center;
    font-size: 92px;
    font-weight: 300;
    letter-spacing: 6px;
    color: var(--logo-ink);
    line-height: 1;
  }
  .contact-line {
    display: flex;
    align-items: center;
    gap: 8px;
    margin: 0;
  }
  .contact-icon {
    width: 20px;
    height: 20px;
    flex: none;
  }
  .address {
    position: absolute;
    left: 80px;
    bottom: 72px;
    font-size: 23px;
    line-height: 1.3;
    font-style: normal;
  }
  .address .contact-icon {
    width: 26px;
    height: 26px;
  }
  .address-lines {
    display: flex;
    flex-direction: column;
  }
  .contacts {
    position: absolute;
    right: 60px;
    top: 288px;
    font-size: 23px;
    line-height: 1.25;
    display: flex;
    flex-direction: column;
    align-items: flex-start;
  }
  .contacts .indent { padding-left: 48px; }
  .contacts .email { font-size: 21px; }
</style>
</head>
<body>
<main class="canvas">
  <article class="business-card">
    <div class="card-pattern" role="img" aria-label="Faint dark paisley and floral pattern covering the card"></div>

    <h1 class="brand-name">DELLA</h1>

    <address class="address contact-line">
      <svg class="contact-icon" viewBox="0 0 24 24" aria-hidden="true" style="align-self:flex-start;margin-top:2px">
        <path d="M12 3 2 12h3v9h5v-6h4v6h5v-9h3z" fill="var(--accent)"/>
      </svg>
      <span class="address-lines">
        <span>5417 Larkmoor Rd.</span>
        <span>#309 Ember Court Arcade</span>
        <span>Va.Beach, Va 23987</span>
      </span>
    </address>

    <div class="contacts">
      <p class="contact-line indent">
        <svg class="contact-icon" viewBox="0 0 24 24" aria-hidden="true">
          <path d="M6.6 10.8a15 15 0 0 0 6.6 6.6l2.2-2.2a1 1 0 0 1 1-.25 11.4 11.4 0 0 0 3.6.57 1 1 0 0 1 1 1V20a1 1 0 0 1-1 1A17 17 0 0 1 3 4a1 1 0 0 1 1-1h3.5a1 1 0 0 1 1 1 11.4 11.4 0 0 0 .57 3.6 1 1 0 0 1-.25 1z" fill="none" stroke="var(--accent)" stroke-width="2"/>
        </svg>
        <span>757 386 5049</span>
      </p>
      <p class="contact-line indent">
        <svg class="contact-icon" viewBox="0 0 24 24" aria-hidden="true">
          <rect x="6" y="2" width="12" height="6" fill="var(--accent)"/>
          <rect x="2" y="9" width="20" height="9" rx="2" fill="var(--accent)"/>
          <rect x="6" y="14" width="12" height="8" fill="var(--card-base)" stroke="var(--accent)" stroke-width="2"/>
        </svg>
        <span>757 386 2613</span>
      </p>
      <p class="contact-line email">
        <svg class="contact-icon" viewBox="0 0 24 24" aria-hidden="true">
          <rect x="2" y="5" width="20" height="15" fill="none" stroke="var(--accent)" stroke-width="2"/>
          <path d="M6 11l4 4 8-8" fill="none" stroke="var(--accent)" stroke-width="2.5"/>
        </svg>
        <span>dellamode@quillbox.com</span>
      </p>
    </div>
  </article>
</main>
</body>
</html>
```